Company service wheel graphic

A graphic demonstrating all the services the company offers.
I have hand drawn and written up on the attached the content that is required. Also attached is our company logo so you have a sense of the colour scheme of the logo.
This will eventually go into a company brochure, be used on our website etc.

Target Market(s)

Local GOvernment and other professionals who work in the sport, recreation and leisure industries

Industry/Entity Type

Sports, recreation, leisure, aquatics

Font styles to use
Other font styles liked:
• Calibri

Colors
0054AA
0677BA
7BADD7
CADEEF
E8F1F8

Requirements
Must have
• An eye catching graphic that captures all the information in the hand drawn atachement.
Nice to have
• Each quadrant in the circle to have its own colour, that links to the company logo

```html
<!DOCTYPE html>
<html lang="en">
<head>
<meta charset="utf-8">
<title>Service Wheel</title>
<link rel="stylesheet" href="https://fonts.googleapis.com/css2?family=Barlow+Condensed:wght@500;600;700&display=swap">
<style>
  :root {
    --navy: #252060;
    --navy-core: #2a2866;
    --sky: #1aace9;
    --mist: #efefef;
    --core-blue: #1070b8;
    --core-grey: #dcdddd;
    --ring-mid: #1587d2;
    --ring-pale: #7cc3e5;
    --frame: #35302e;
    --dot: #1273bd;
    --ink: #2d2d2d;
    --white: #ffffff;
    --pale-label: #a9d9f1;
  }
  html, body {
    margin: 0;
    padding: 0;
    width: 1200px;
    height: 1200px;
    overflow: hidden;
    background: var(--white);
  }
  .service-wheel {
    display: block;
    width: 1200px;
    height: 1200px;
    font-family: "Barlow Condensed", "Arial Narrow", sans-serif;
  }
  .audience-label { font-size: 52px; font-weight: 700; fill: var(--navy); }
  .service-line { font-size: 31px; font-weight: 600; }
  .service-line--dark { fill: var(--ink); }
  .service-line--light { fill: var(--white); }
  .pillar-label { font-size: 30px; font-weight: 600; }
  .pillar-label--pale { fill: var(--pale-label); }
  .pillar-label--navy { fill: var(--navy); }
  .core-title { font-size: 42px; font-weight: 700; fill: var(--white); text-anchor: middle; }
  .banner-text { font-size: 29px; font-weight: 600; fill: var(--sky); text-anchor: middle; }
  .ring-frame { fill: none; stroke: var(--frame); stroke-width: 7; }
  .ring-dot { fill: var(--dot); }
</style>
</head>
<body>
<svg class="service-wheel" viewBox="0 0 1932 1932" xmlns="http://www.w3.org/2000/svg">
  <defs>
    <!-- audience arcs -->
    <path id="arc-aud-tl" d="M166,966 A800 800 0 0 1 966,166"/>
    <path id="arc-aud-tr" d="M966,166 A800 800 0 0 1 1766,966"/>
    <path id="arc-aud-bl" d="M96,966 A870 870 0 0 0 966,1836"/>
    <path id="arc-aud-br" d="M966,1836 A870 870 0 0 0 1836,966"/>
    <!-- service arcs -->
    <path id="arc-tl-1" d="M276,966 A690 690 0 0 1 966,276"/>
    <path id="arc-tl-2" d="M376,966 A590 590 0 0 1 966,376"/>
    <path id="arc-tl-3" d="M461,966 A505 505 0 0 1 966,461"/>
    <path id="arc-tr-1" d="M966,286 A680 680 0 0 1 1646,966"/>
    <path id="arc-tr-2" d="M966,376 A590 590 0 0 1 1556,966"/>
    <path id="arc-tr-3" d="M966,471 A495 495 0 0 1 1461,966"/>
    <path id="arc-bl-1" d="M266,966 A700 700 0 0 0 966,1666"/>
    <path id="arc-bl-2" d="M356,966 A610 610 0 0 0 966,1576"/>
    <path id="arc-bl-3" d="M446,966 A520 520 0 0 0 966,1486"/>
    <path id="arc-br-1" d="M966,1521 A555 555 0 0 0 1521,966"/>
    <path id="arc-br-2" d="M966,1636 A670 670 0 0 0 1636,966"/>
    <!-- pillar arcs -->
    <path id="arc-pl-tl" d="M771,966 A195 195 0 0 1 966,771"/>
    <path id="arc-pl-tr" d="M966,766 A200 200 0 0 1 1166,966"/>
    <path id="arc-pl-bl" d="M761,966 A205 205 0 0 0 966,1171"/>
    <path id="arc-pl-br-1" d="M966,1171 A205 205 0 0 0 1171,966"/>
    <path id="arc-pl-br-2" d="M966,1206 A240 240 0 0 0 1206,966"/>
    <clipPath id="core-clip">
      <rect x="681" y="685" width="569" height="565" rx="78"/>
    </clipPath>
  </defs>

  <!-- outer frame -->
  <circle class="ring-frame" cx="966" cy="966" r="922"/>
  <circle class="ring-dot" cx="966" cy="144" r="9"/>
  <circle class="ring-dot" cx="127" cy="964" r="9"/>
  <circle class="ring-dot" cx="1797" cy="964" r="9"/>
  <circle class="ring-dot" cx="966" cy="1796" r="9"/>

  <!-- quadrant disc -->
  <g class="quadrants">
    <path fill="var(--mist)" d="M966,966 L199,966 A767 767 0 0 1 966,199 Z"/>
    <path fill="var(--sky)" d="M966,966 L966,199 A767 767 0 0 1 1733,966 Z"/>
    <path fill="var(--mist)" d="M966,966 L1733,966 A767 767 0 0 1 966,1733 Z"/>
    <path fill="var(--sky)" d="M966,966 L966,1733 A767 767 0 0 1 199,966 Z"/>
  </g>

  <!-- audience labels -->
  <text class="audience-label" text-anchor="middle"><textPath href="#arc-aud-tl" startOffset="43.9%">LOCAL + STATE GOVERNMENT</textPath></text>
  <text class="audience-label" text-anchor="middle"><textPath href="#arc-aud-tr" startOffset="53.3%">SPORT + LEISURE FACILITY MANAGERS</textPath></text>
  <text class="audience-label" text-anchor="middle"><textPath href="#arc-aud-bl" startOffset="47.8%">INVESTORS, DEVELOPERS, ARCHITECTS + DESIGNERS</textPath></text>
  <text class="audience-label" text-anchor="middle"><textPath href="#arc-aud-br" startOffset="52.8%">SPORT + RECREATION + COMMUNITY PROVIDERS</textPath></text>

  <!-- services: government -->
  <text class="service-line service-line--dark" text-anchor="middle"><textPath href="#arc-tl-1" startOffset="45.6%">Design Strategies  |  Indoor + Outdoors Spaces</textPath></text>
  <text class="service-line service-line--dark" text-anchor="middle"><textPath href="#arc-tl-2" startOffset="48.9%">Sport + Recreation Strategies  |  Sport + Reaction Strategies</textPath></text>
  <text class="service-line service-line--dark" text-anchor="middle"><textPath href="#arc-tl-3" startOffset="48.9%">Feasibility Studies  |  Community + Stakeholders Research</textPath></text>

  <!-- services: facility managers -->
  <text class="service-line service-line--light" text-anchor="middle"><textPath href="#arc-tr-1" startOffset="50%">Activating Underutilised Assets  /  Income + Revenue Generation Strategies</textPath></text>
  <text class="service-line service-line--light" text-anchor="middle"><textPath href="#arc-tr-2" startOffset="50%">Mystery Shopper + Business Health Checks  /  Financial + Funding Strategies</textPath></text>
  <text class="service-line service-line--light" text-anchor="middle"><textPath href="#arc-tr-3" startOffset="51.1%">Management Support  /  Business Planning</textPath></text>

  <!-- services: investors and designers -->
  <text class="service-line service-line--light" text-anchor="middle"><textPath href="#arc-bl-1" startOffset="50%">Physical Activity Strategies | Specific Cohort Strategies / Sport + Program Specific Strategies</textPath></text>
  <text class="service-line service-line--light" text-anchor="middle"><textPath href="#arc-bl-2" startOffset="50%">Active Recreation Strategies  /  Community Program Development</textPath></text>
  <text class="service-line service-line--light" text-anchor="middle"><textPath href="#arc-bl-3" startOffset="48.9%">Trends + Insights  /  Health Profiling</textPath></text>

  <!-- services: community providers -->
  <text class="service-line service-line--dark" text-anchor="middle"><textPath href="#arc-br-1" startOffset="53.3%">Community Impact Monitoring  /  Social Value</textPath></text>
  <text class="service-line service-line--dark" text-anchor="middle"><textPath href="#arc-br-2" startOffset="50.6%">Community Outcomes + KPIs  /  Contact Monitoring</textPath></text>

  <!-- core square -->
  <g class="core-square" clip-path="url(#core-clip)">
    <rect x="681" y="685" width="285" height="281" fill="var(--core-blue)"/>
    <rect x="966" y="685" width="284" height="281" fill="var(--core-grey)"/>
    <rect x="681" y="966" width="285" height="284" fill="var(--core-grey)"/>
    <rect x="966" y="966" width="284" height="284" fill="var(--core-blue)"/>
  </g>

  <!-- engagement ring -->
  <g class="core-ring">
    <path fill="var(--ring-mid)" d="M966,966 L791,966 A175 175 0 0 1 966,791 Z"/>
    <path fill="var(--ring-pale)" d="M966,966 L966,791 A175 175 0 0 1 1141,966 Z"/>
    <path fill="var(--ring-mid)" d="M966,966 L1141,966 A175 175 0 0 1 966,1141 Z"/>
    <path fill="var(--ring-pale)" d="M966,966 L966,1141 A175 175 0 0 1 791,966 Z"/>
  </g>
  <circle cx="966" cy="966" r="147" fill="var(--navy-core)"/>

  <!-- pillar labels -->
  <text class="pillar-label pillar-label--pale" text-anchor="middle"><textPath href="#arc-pl-tl" startOffset="50%">Planning</textPath></text>
  <text class="pillar-label pillar-label--navy" text-anchor="middle"><textPath href="#arc-pl-tr" startOffset="50%">Management</textPath></text>
  <text class="pillar-label pillar-label--navy" text-anchor="middle"><textPath href="#arc-pl-bl" startOffset="50%">Growing Participation</textPath></text>
  <text class="pillar-label pillar-label--pale" text-anchor="middle"><textPath href="#arc-pl-br-1" startOffset="50%">Community Impact</textPath></text>
  <text class="pillar-label pillar-label--pale" text-anchor="middle"><textPath href="#arc-pl-br-2" startOffset="50%">+ Outcomes</textPath></text>

  <!-- core title -->
  <text class="core-title" x="966" y="910">COMMUNITY</text>
  <text class="core-title" x="966" y="958">+</text>
  <text class="core-title" x="966" y="1006">STAKEHOLDER</text>
  <text class="core-title" x="966" y="1053">ENGAGEMENT</text>

  <!-- banners -->
  <rect x="725" y="615" width="482" height="71" rx="16" fill="var(--navy)"/>
  <text class="banner-text" x="966" y="660">Community, Aquatic + Recreation Facilities</text>
  <rect x="725" y="1240" width="482" height="71" rx="16" fill="var(--navy)"/>
  <text class="banner-text" x="966" y="1285">Community Activation</text>
</svg>
</body>
</html>
```